Template Flyer- Lunarcore Pilates & Yoga

I am wanting a template 1 page flyer designed to use on the back ground of newsletter (faded background) and for our advertising posters in A4, A3, for Facebook and Instagram compatibility.

I have loaded an example from another Studio called Fernbrook (file 3)- each time they have a new workshop to advertise a picture is placed in the little circle (so this is something I would want to do too where I can load a new picture each time a new workshop is running)- They have used the flyer like a water mark...I like this.

Our colour palette is what is on our logos and you can also visit our website for a feel for what we like www.lunarcorepilates.com.au

I need some of the designs edited a bit more and because of the time difference, there seems to be a 24hour period where we communicate with each other. May I please request another 2 days extension

Need extra days to review

Requirements
Must have
• Id like to have a picture in the back ground. My favourite back ground that has been produced so far is a background of both picture file 9 and 10 in either.
Nice to have
• 3 picture circles options to advertise the events/workshops I have each year.
• Brush stroke style circles (see picture attached)rather then smooth circles for the picture area (in a grey tone)
Should not have
• No BLACK colour writing or black circles

```html
<!DOCTYPE html>
<html lang="en">
<head>
<meta charset="utf-8">
<title>Lunarcore Pilates &amp; Yoga – Workshop Flyer</title>
<link rel="stylesheet" href="https://fonts.googleapis.com/css2?family=Jost:wght@400;500;600;700&display=swap">
<style>
  :root {
    --backdrop: #e4e2de;
    --paper: #f1f1ef;
    --brand-blue: #4a8fb0;
    --wave-blue: #3f86a8;
    --wave-grey: #8d877f;
    --text-grey: #5b5a58;
    --photo-light: #f2f1ed;
    --photo-mid: #d9d6cf;
    --photo-floor: #8f8c88;
  }
  * { margin: 0; padding: 0; box-sizing: border-box; }
  html, body {
    width: 1200px;
    height: 984px;
    overflow: hidden;
    background: var(--backdrop);
    font-family: "Jost", "Futura", sans-serif;
  }
  .flyer {
    position: absolute;
    left: 268px;
    top: 22px;
    width: 664px;
    height: 940px;
    background: var(--paper);
    box-shadow: 0 6px 24px rgba(60, 55, 50, 0.25);
    overflow: hidden;
  }
  .studio-photo {
    position: absolute;
    left: 0;
    top: 0;
    width: 664px;
    height: 490px;
    background: linear-gradient(180deg, var(--photo-light) 0%, var(--photo-light) 38%, var(--photo-mid) 55%, var(--photo-floor) 75%, var(--photo-mid) 100%);
  }
  .wave-divider {
    position: absolute;
    left: 0;
    top: 300px;
    width: 664px;
    height: 200px;
  }
  .flyer-copy {
    position: absolute;
    left: 0;
    top: 492px;
    width: 664px;
    text-align: center;
    color: var(--text-grey);
  }
  .intro {
    font-size: 34px;
    font-weight: 400;
    line-height: 1.1;
  }
  .headline {
    font-size: 50px;
    font-weight: 700;
    color: var(--brand-blue);
    line-height: 1.1;
    letter-spacing: 0.5px;
  }
  .event-date {
    margin-top: 16px;
    font-size: 31px;
    font-weight: 400;
    line-height: 1.1;
  }
  .event-date sup { font-size: 17px; }
  .event-time {
    font-size: 29px;
    font-weight: 600;
    color: var(--brand-blue);
    line-height: 1.15;
  }
  .pricing {
    margin-top: 18px;
    font-size: 29px;
    line-height: 1.2;
  }
  .pricing strong { color: var(--brand-blue); font-weight: 600; }
  .website {
    margin-top: 24px;
    font-size: 17px;
    letter-spacing: 5px;
    font-weight: 500;
  }
  .brand {
    margin-top: 22px;
    display: flex;
    align-items: center;
    justify-content: center;
    gap: 14px;
  }
  .brand-dot {
    width: 44px;
    height: 44px;
    border-radius: 50%;
    background: var(--brand-blue);
  }
  .brand-name {
    font-size: 34px;
    font-weight: 500;
    color: var(--brand-blue);
  }
  .tagline {
    margin-top: 4px;
    font-size: 16px;
    letter-spacing: 1.5px;
    color: var(--brand-blue);
  }
</style>
</head>
<body>
  <main class="flyer">
    <div class="studio-photo" role="img" aria-label="Bright white pilates and yoga studio with mats, bolsters and cork blocks laid out on the floor"></div>

    <svg class="wave-divider" viewBox="0 0 664 200" aria-hidden="true">
      <path d="M0 150 C 140 175, 260 150, 380 105 C 480 68, 580 58, 664 62 L664 200 L0 200 Z" fill="var(--paper)"/>
      <path d="M0 150 C 140 175, 260 150, 380 105 C 480 68, 580 58, 664 62" fill="none" stroke="var(--wave-blue)" stroke-width="7"/>
      <path d="M0 164 C 150 182, 270 162, 390 120 C 490 86, 590 78, 664 82" fill="none" stroke="var(--wave-grey)" stroke-width="3"/>
    </svg>

    <section class="flyer-copy">
      <p class="intro">Pilates &amp; yoga for your</p>
      <h1 class="headline">MIND, BODY &amp; SOUL</h1>
      <p class="event-date">SUNDAY 18<sup>TH</sup> MARCH</p>
      <p class="event-time">6:30PM - 8:00PM</p>
      <p class="pricing">Investment <strong>$540</strong> Regular or<br><strong>$35</strong> For Annual Members</p>
      <p class="website">www.lunarcorepilates.com.au</p>
      <div class="brand">
        <span class="brand-dot"></span>
        <span class="brand-name">Lunarcore Pilates &amp; Yoga</span>
      </div>
      <p class="tagline">move well and live well daily</p>
    </section>
  </main>
</body>
</html>
```